Pull Up Banner Design for finance broker

We are requiring a design for pull up banners. KTV Finance provides finance services for a range of business equipment purchases including trucks, excavators, vehicle hoists and other industrial equipment. We are looking for a generic design that is not industry specific that we can place in dealerships that refer their clients to us to obtain their finance. The image we have selected (Attached) should be faint in the back ground (Or if you have alternative ideas/layout/image)

Size 2000mm x 800mm

Target Market(s)

Businesses requiring finance for equipment purchases

Industry/Entity Type

Finance

Requirements
Must have
• Banner to include the following text:
• Key Text:
• "Equipment Finance"
• "25+ Lenders" (Feature)
• Information Text:
• "Start-up / Existing Businesses"
• "New / Used"
• "Fast Approvals"
• "Flexible Options"
• Company/contact Text:
• "An Entire Company working for you" (Slogan)
• "1300 864 592"
• "www.ktvfinance.example.au"
• Logo: Attached - colours can be reversed (Banner colours to be used from this
Nice to have
• preference is darker background - not white

```html
<!DOCTYPE html>
<html lang="en">
<head>
<meta charset="utf-8">
<title>KTV Finance – Equipment Finance Pull Up Banner</title>
<link href="https://fonts.googleapis.com/css2?family=Roboto+Condensed:wght@700&family=Arimo:wght@400;700&display=swap" rel="stylesheet">
<style>
  :root {
    --page: #ffffff;
    --orange: #ef6c22;
    --orange-deep: #e0601a;
    --navy: #2b313c;
    --white: #ffffff;
  }
  html, body {
    margin: 0;
    padding: 0;
    width: 1200px;
    height: 1000px;
    overflow: hidden;
    background: var(--page);
  }
  .banner {
    position: absolute;
    left: 435px;
    top: 88px;
    width: 330px;
    height: 824px;
    overflow: hidden;
    background: var(--orange);
  }
  .banner__backdrop {
    position: absolute;
    inset: 0;
    background:
      radial-gradient(circle at 30% 10%, rgba(180,70,10,0.35), transparent 40%),
      radial-gradient(circle at 70% 45%, rgba(200,80,15,0.3), transparent 45%),
      radial-gradient(circle at 20% 75%, rgba(190,75,12,0.3), transparent 40%),
      linear-gradient(180deg, var(--orange-deep), var(--orange));
  }
  .headline {
    position: absolute;
    left: 0;
    top: 79px;
    width: 330px;
    height: 151px;
    background: var(--navy);
    color: var(--white);
    font-family: "Roboto Condensed", sans-serif;
    font-weight: 700;
    font-size: 52px;
    line-height: 58px;
    text-align: center;
    display: flex;
    flex-direction: column;
    justify-content: center;
  }
  .feature {
    position: absolute;
    left: 0;
    width: 330px;
    top: 280px;
    margin: 0;
    text-align: center;
    color: var(--white);
    font-family: "Roboto Condensed", sans-serif;
    font-weight: 700;
    font-size: 44px;
  }
  .benefits {
    position: absolute;
    left: 0;
    top: 372px;
    margin: 0;
    padding: 0;
    list-style: none;
    font-family: "Roboto Condensed", sans-serif;
    font-weight: 700;
    font-size: 24px;
    line-height: 29px;
    color: var(--navy);
  }
  .benefits li {
    position: relative;
    padding-left: 81px;
    margin-bottom: 10px;
  }
  .benefits li::before {
    content: "";
    position: absolute;
    left: 0;
    top: 15px;
    width: 60px;
    height: 2px;
    background: var(--navy);
  }
  .benefits li::after {
    content: "";
    position: absolute;
    left: 53px;
    top: 9px;
    width: 14px;
    height: 14px;
    border-radius: 50%;
    background: var(--navy);
  }
  .company {
    position: absolute;
    left: 0;
    width: 330px;
    top: 692px;
    text-align: center;
    color: var(--white);
    font-family: "Arimo", sans-serif;
  }
  .company__name {
    display: inline-flex;
    align-items: center;
    gap: 8px;
    font-weight: 700;
    font-size: 28px;
    letter-spacing: 1px;
  }
  .company__mark {
    width: 26px;
    height: 26px;
    background: var(--white);
  }
  .company__slogan {
    font-size: 11.5px;
    margin-top: 8px;
  }
  .company__phone {
    font-weight: 700;
    font-size: 21px;
    margin-top: 10px;
    line-height: 22px;
  }
  .company__web {
    font-size: 11px;
  }
</style>
</head>
<body>
  <div class="banner">
    <div class="banner__backdrop" role="img" aria-label="Faint background image of interlocking machine gears in orange tones"></div>
    <div class="headline"><span>EQUIPMENT</span><span>FINANCE</span></div>
    <p class="feature">25+ Lenders</p>
    <ul class="benefits">
      <li>Start-up / Existing<br>Businesses</li>
      <li>New / Used</li>
      <li>Fast Approvals</li>
      <li>Flexible Options</li>
    </ul>
    <div class="company">
      <div class="company__name"><span class="company__mark"></span>KTV FINANCE</div>
      <div class="company__slogan">An Entire Company working for you</div>
      <div class="company__phone">1300 864 592</div>
      <div class="company__web">www.ktvfinance.example.au</div>
    </div>
  </div>
</body>
</html>
```